Fair Lend Guide's Mortgage Lantern

For FairLendGuide.org - Creating a sequence of web pages for consumers to understand their mortgage through Mortgage Lantern. There are six pages - want the designer to be willing to design and code those six pages. Most of the pages are very similar.

```html
<!DOCTYPE html>
<html lang="en">
<head>
<meta charset="utf-8">
<title>Fair Lend Guide – Mortgage Central</title>
<link href="https://fonts.googleapis.com/css2?family=Poppins:wght@400;500;600;700&display=swap" rel="stylesheet">
<style>
  :root {
    --page-bg: #edf1fa;
    --brand-blue: #1652c8;
    --brand-green: #08ad59;
    --card-bg: #ffffff;
    --label: #575757;
    --footer-text: #444444;
    --active-start: #06a064;
    --active-end: #1456c9;
    --icon-start: #12b46e;
    --icon-end: #1f5bd0;
  }
  * { box-sizing: border-box; margin: 0; padding: 0; }
  html, body { width: 1200px; height: 879px; overflow: hidden; }
  body {
    background: var(--page-bg);
    font-family: "Poppins", sans-serif;
    position: relative;
  }
  .decor { position: absolute; inset: 0; width: 1200px; height: 879px; }
  .brand {
    position: absolute; top: 108px; left: 0; width: 1200px;
    text-align: center;
    font-size: 40px; font-weight: 500; color: var(--brand-blue);
    letter-spacing: -0.5px;
  }
  .brand-mark {
    position: absolute; top: 30px; left: 558px;
    width: 84px; height: 72px; border-radius: 10px;
    background: var(--brand-blue);
  }
  .page-title {
    position: absolute; top: 208px; left: 0; width: 1200px;
    text-align: center;
    font-size: 44px; font-weight: 700; color: var(--brand-blue);
    letter-spacing: -0.3px;
  }
  .tool-grid {
    position: absolute; top: 311px; left: 211px;
    display: grid;
    grid-template-columns: repeat(4, 184px);
    grid-auto-rows: 172px;
    column-gap: 22px; row-gap: 22px;
  }
  .tool-card {
    background: var(--card-bg);
    border-radius: 12px;
    display: flex; flex-direction: column; align-items: center;
    padding-top: 27px;
    text-decoration: none;
    box-shadow: 0 2px 10px rgba(40, 70, 140, 0.05);
  }
  .tool-icon {
    width: 66px; height: 66px; border-radius: 12px;
    background: linear-gradient(135deg, var(--icon-start), var(--icon-end));
    opacity: 0.85;
  }
  .tool-label {
    margin-top: 13px;
    font-size: 15px; font-weight: 500; line-height: 19px;
    color: var(--label); text-align: center;
  }
  .tool-card.is-active {
    background: linear-gradient(90deg, var(--active-start) 30%, var(--active-end));
  }
  .tool-card.is-active .tool-label { color: #ffffff; }
  .tool-card.is-active .tool-icon { background: rgba(255,255,255,0.85); }
  .site-footer {
    position: absolute; top: 779px; left: 0; width: 1200px;
    text-align: center;
    font-size: 15px; color: var(--footer-text);
  }
  .site-footer .divider { margin: 0 12px; }
</style>
</head>
<body>
  <svg class="decor" viewBox="0 0 1200 879" aria-hidden="true">
    <path d="M0 0 H381 C290 22 235 80 190 160 C130 272 70 392 0 466 Z" fill="var(--brand-green)"/>
    <path d="M1200 703 C1120 742 1010 760 960 780 C910 802 890 842 881 879 H1200 Z" fill="var(--brand-blue)"/>
  </svg>

  <div class="brand-mark" aria-hidden="true"></div>
  <div class="brand">FairLendGuide</div>

  <h1 class="page-title">Mortgage Central</h1>

  <nav class="tool-grid">
    <a class="tool-card is-active" href="#"><span class="tool-icon" role="img" aria-label="Profile document with pencil icon"></span><span class="tool-label">Edit Mortgage<br>Profile</span></a>
    <a class="tool-card" href="#"><span class="tool-icon" role="img" aria-label="Qualification documents icon"></span><span class="tool-label">Maximum Mortgage<br>Qualifications</span></a>
    <a class="tool-card" href="#"><span class="tool-icon" role="img" aria-label="House with dollar coin icon"></span><span class="tool-label">Specific Mortgage<br>Amount</span></a>
    <a class="tool-card" href="#"><span class="tool-icon" role="img" aria-label="House with banknote icon"></span><span class="tool-label">Specific Mortgage<br>Payment</span></a>
    <a class="tool-card" href="#"><span class="tool-icon" role="img" aria-label="Family under roof icon"></span><span class="tool-label">Conventional<br>Mortgage Options</span></a>
    <a class="tool-card" href="#"><span class="tool-icon" role="img" aria-label="House and dollar exchange icon"></span><span class="tool-label">FHA Mortgage<br>Options</span></a>
    <a class="tool-card" href="#"><span class="tool-icon" role="img" aria-label="Signed contract with house icon"></span><span class="tool-label">VA Mortgage<br>Options</span></a>
    <a class="tool-card" href="#"><span class="tool-icon" role="img" aria-label="Approved home checklist icon"></span><span class="tool-label">USDA Mortgage<br>Options</span></a>
  </nav>

  <footer class="site-footer">Copyright 2023 by Fair Lend Guide. Terms Of Use<span class="divider">|</span>Privacy Statement</footer>
</body>
</html>
```